Educational Software Company Needs Banner Ads Prompting an Event

We are looking for a series of banner ads (to be used in conjunction with plexa adlink), pushing people to register for our upcoming road tour, Hallway Heroes. Hallway Heroes is a series of one-day workshops that offer best practices for individuals in the educational operations industry. To learn more about the event please view the website at: hallwayheroes.gradefinch.com.

Feel free to use any of the language from the website, logo (attached), and the hex colors which are listed in the "must have" section below.

Some language that we have use on other marketing materials:
"We're Hitting the Road!"
Our 2014 road tour is heading to a city near you!
"Invest in Your Success"
"We're Hitting the Road, and Heading Your Way!"
"Hallway Heroes - A free, one-day workshop offering lessons for success"
"Seating is Limited - Register Today!"

Supported ad sizes and specs:
250 x 250 square
200 x 200 square
468 x 60 banner
728 x 90 leaderboard
300 x 250 inline rectangle
120 x 600 skyscraper
160 x 600 wide skyscrapper
320 x 50 mobile leaderboard

The call to action for the ad should be to "Register Today!"

Target Market(s)

educational operations professionals, i.e. maintenance directors, energy managers, superintendents, business officers etc...

Industry/Entity Type

Marketing

Requirements
Must have
• event logo and/or event name using event colors; CTA button reading "Register Today!"

Colors:
HH – Red #A63515
R: 166
G: 53
B: 21

HH – Dark Gray #726658
R: 114
G: 102
B: 88

HH – Light Gray #CECECE
R: 206
G: 206
B: 206

HH – Orange #EDA45B
R: 237
G: 164
B: 91
Nice to have
• Consider using list of stops on larger banner ads.

1/14/2014 Seattle, CA
1/16/2014 Phoenix, CA
1/21/2014 Sacramento, CA
1/23/2014 Ontario, CA
2/13/2014 Kilgore, TX
2/11/2014 Coppell, TX
TBD Schaumburg, IL

```html
<!DOCTYPE html>
<html lang="en">
<head>
<meta charset="utf-8">
<title>Hallway Heroes – 2014 Road Tour Banner Set</title>
<link rel="stylesheet" href="https://fonts.googleapis.com/css2?family=Kreon:wght@400;700&family=Dosis:wght@500;600&family=Bree+Serif&display=swap">
<style>
  :root {
    --hh-red: #a63515;
    --hh-red-dark: #8a2b12;
    --hh-dark-gray: #726658;
    --hh-light-gray: #cecece;
    --hh-orange: #eda45b;
    --sky: #aadcdc;
    --hill: #7d8f6a;
    --grass: #97a24a;
    --road: #5e4a3e;
    --paper: #ffffff;
  }
  * { box-sizing: border-box; margin: 0; padding: 0; }
  html, body { width: 1200px; height: 623px; overflow: hidden; background: var(--paper); }
  body { position: relative; font-family: "Kreon", serif; color: var(--hh-red); }

  .ad { position: absolute; background: var(--sky); overflow: hidden; }
  .ad--sky-a { left: 46px; top: 10px; width: 161px; height: 600px; }
  .ad--sky-b { left: 218px; top: 10px; width: 160px; height: 600px; }
  .ad--leader-a { left: 395px; top: 13px; width: 728px; height: 90px; }
  .ad--leader-b { left: 395px; top: 118px; width: 728px; height: 90px; }
  .ad--rect-a { left: 395px; top: 228px; width: 300px; height: 250px; }
  .ad--rect-b { left: 709px; top: 228px; width: 300px; height: 250px; }

  .brand { position: absolute; text-align: center; }
  .brand__dot { display: block; margin: 0 auto; border-radius: 50%; background: var(--hh-orange); }
  .brand__name { display: block; font-family: "Bree Serif", serif; font-weight: 400; color: var(--hh-red); line-height: 1; letter-spacing: 1px; }

  .headline { position: absolute; text-align: center; font-weight: 400; line-height: 1.2; color: var(--hh-red); }
  .headline strong { font-weight: 700; }

  .cta {
    position: absolute; border-radius: 50%; background: var(--hh-red);
    box-shadow: 0 0 0 2px var(--hh-red-dark), 0 2px 3px rgba(0,0,0,.3);
    display: flex; align-items: center; justify-content: center; text-align: center;
    font-family: "Dosis", sans-serif; font-weight: 600; color: var(--hh-orange); line-height: 1.2;
  }

  .scene { position: absolute; background: linear-gradient(180deg, var(--sky) 0%, var(--hill) 45%, var(--road) 72%, var(--grass) 100%); }

  .ribbon { position: absolute; }
  .ribbon__label { position: absolute; left: 0; right: 0; text-align: center; font-family: "Dosis", sans-serif; font-weight: 500; color: var(--hh-orange); }

  .stops { position: absolute; font-family: "Kreon", serif; font-weight: 700; font-size: 9.5px; line-height: 11.6px; color: var(--hh-red); }
  .stops li { list-style: none; display: flex; }
  .stops .date { width: 64px; }

  .dest-title { position: absolute; font-family: "Dosis", sans-serif; font-weight: 500; font-size: 18px; letter-spacing: .5px; color: var(--hh-dark-gray); }
  .dest-rule { position: absolute; height: 1px; background: var(--hh-red); }
</style>
</head>
<body>

<!-- Skyscraper A -->
<section class="ad ad--sky-a">
  <div class="brand" style="left:0;right:0;top:22px;">
    <span class="brand__dot" style="width:38px;height:38px;margin-bottom:16px;"></span>
    <span class="brand__name" style="font-size:23px;">HALLWAY<br>HEROES</span>
  </div>
  <p class="headline" style="left:0;right:0;top:172px;font-size:25px;">Our <strong>2014</strong><br>road tour is<br>heading<br>to a city<br>near you!</p>
  <a class="cta" style="left:37px;top:394px;width:82px;height:82px;font-size:15px;">Register<br>Today!</a>
  <div class="scene" role="img" aria-label="Illustration of a red station wagon with luggage on the roof driving past mountains and pine trees" style="left:0;top:480px;width:161px;height:120px;"></div>
</section>

<!-- Skyscraper B -->
<section class="ad ad--sky-b">
  <div class="brand" style="left:0;right:0;top:22px;">
    <span class="brand__dot" style="width:38px;height:38px;margin-bottom:16px;"></span>
    <span class="brand__name" style="font-size:23px;">HALLWAY<br>HEROES</span>
  </div>
  <svg class="ribbon" width="160" height="185" style="left:0;top:203px;" viewBox="0 0 160 185" aria-hidden="true">
    <polygon points="6,40 154,40 154,175 6,150" fill="var(--paper)"/>
    <polygon points="0,30 6,30 6,48" fill="var(--hh-red-dark)"/>
    <polygon points="160,30 154,30 154,48" fill="var(--hh-red-dark)"/>
    <rect x="0" y="2" width="160" height="32" fill="var(--hh-red)"/>
  </svg>
  <span class="ribbon__label" style="top:208px;font-size:16px;">DESTINATION</span>
  <ul class="stops" style="left:12px;top:248px;">
    <li><span class="date">1/14/2014</span>Seattle, CA</li>
    <li><span class="date">1/16/2014</span>Phoenix, CA</li>
    <li><span class="date">1/21/2014</span>Sacramento, CA</li>
    <li><span class="date">1/23/2014</span>Ontario, CA</li>
    <li><span class="date">2/13/2014</span>Kilgore, TX</li>
    <li><span class="date">2/11/2014</span>Coppell, TX</li>
    <li>TBD Schaumburg, IL</li>
  </ul>
  <a class="cta" style="left:38px;top:394px;width:82px;height:82px;font-size:15px;">Register<br>Today!</a>
  <div class="scene" role="img" aria-label="Illustration of a red station wagon with luggage on the roof driving past mountains and pine trees" style="left:0;top:480px;width:160px;height:120px;"></div>
</section>

<!-- Leaderboard A -->
<section class="ad ad--leader-a">
  <div class="brand" style="left:10px;top:18px;width:62px;">
    <span class="brand__dot" style="width:18px;height:18px;margin-bottom:5px;"></span>
    <span class="brand__name" style="font-size:11px;">HALLWAY<br>HEROES</span>
  </div>
  <p class="headline" style="left:110px;width:330px;top:22px;font-size:22px;">Our <strong>2014</strong> road tour is<br>heading to a city near you!</p>
  <div class="scene" role="img" aria-label="Illustration of a red station wagon with luggage on the roof driving past mountains" style="left:505px;top:0;width:223px;height:90px;"></div>
  <a class="cta" style="left:445px;top:5px;width:80px;height:80px;font-size:14px;">Register<br>Today!</a>
</section>

<!-- Leaderboard B -->
<section class="ad ad--leader-b">
  <div class="brand" style="left:10px;top:18px;width:62px;">
    <span class="brand__dot" style="width:18px;height:18px;margin-bottom:5px;"></span>
    <span class="brand__name" style="font-size:11px;">HALLWAY<br>HEROES</span>
  </div>
  <svg class="ribbon" width="345" height="90" style="left:114px;top:0;" viewBox="0 0 345 90" aria-hidden="true">
    <rect x="0" y="0" width="13" height="90" fill="var(--hh-red)"/>
    <polygon points="13,4 340,4 310,80 13,80" fill="var(--paper)"/>
  </svg>
  <h2 class="dest-title" style="left:141px;top:7px;">DESTINATION</h2>
  <span class="dest-rule" style="left:262px;top:18px;width:158px;"></span>
  <ul class="stops" style="left:143px;top:31px;">
    <li><span class="date">1/14/2014</span>Seattle, CA</li>
    <li><span class="date">1/16/2014</span>Phoenix, CA</li>
    <li><span class="date">1/21/2014</span>Sacramento, CA</li>
  </ul>
  <ul class="stops" style="left:300px;top:31px;">
    <li><span class="date">1/23/2014</span>Ontario, CA</li>
    <li><span class="date">2/13/2014</span>Kilgore, TX</li>
    <li><span class="date">2/11/2014</span>Coppell, TX</li>
    <li>TBD Schaumburg, IL</li>
  </ul>
  <div class="scene" role="img" aria-label="Illustration of a red station wagon with luggage on the roof driving past mountains" style="left:505px;top:0;width:223px;height:90px;"></div>
  <a class="cta" style="left:440px;top:5px;width:80px;height:80px;font-size:14px;">Register<br>Today!</a>
</section>

<!-- Rectangle A -->
<section class="ad ad--rect-a">
  <div class="brand" style="left:12px;top:22px;width:100px;">
    <span class="brand__dot" style="width:32px;height:32px;margin-bottom:12px;"></span>
    <span class="brand__name" style="font-size:17px;">HALLWAY<br>HEROES</span>
  </div>
  <p class="headline" style="left:120px;width:150px;top:14px;font-size:21px;">Our <strong>2014</strong><br>road tour is<br>heading<br>to a city<br>near you!</p>
  <div class="scene" role="img" aria-label="Illustration of a red station wagon with luggage on the roof driving uphill past mountains and pine trees" style="left:0;top:135px;width:300px;height:115px;"></div>
</section>

<!-- Rectangle B -->
<section class="ad ad--rect-b">
  <div class="brand" style="left:14px;top:22px;width:100px;">
    <span class="brand__dot" style="width:32px;height:32px;margin-bottom:12px;"></span>
    <span class="brand__name" style="font-size:17px;">HALLWAY<br>HEROES</span>
  </div>
  <div class="scene" role="img" aria-label="Illustration of a red station wagon with luggage on the roof driving uphill past mountains and pine trees" style="left:0;top:135px;width:300px;height:115px;"></div>
  <svg class="ribbon" width="170" height="170" style="left:112px;top:18px;" viewBox="0 0 170 170" aria-hidden="true">
    <polygon points="16,30 166,30 166,160 16,165" fill="var(--paper)"/>
    <polygon points="0,8 12,8 12,30 0,30 6,19" fill="var(--hh-red-dark)"/>
    <polygon points="170,8 158,8 158,30 170,30 164,19" fill="var(--hh-red-dark)"/>
    <rect x="10" y="4" width="150" height="26" fill="var(--hh-red)"/>
  </svg>
  <span class="ribbon__label" style="left:112px;right:18px;top:24px;font-size:16px;">DESTINATION</span>
  <ul class="stops" style="left:138px;top:65px;">
    <li><span class="date">1/14/2014</span>Seattle, CA</li>
    <li><span class="date">1/16/2014</span>Phoenix, CA</li>
    <li><span class="date">1/21/2014</span>Sacramento, CA</li>
    <li><span class="date">1/23/2014</span>Ontario, CA</li>
    <li><span class="date">2/13/2014</span>Kilgore, TX</li>
    <li><span class="date">2/11/2014</span>Coppell, TX</li>
    <li>TBD Schaumburg, IL</li>
  </ul>
  <a class="cta" style="left:162px;top:162px;width:80px;height:80px;font-size:15px;">Register<br>Today!</a>
</section>

</body>
</html>
```